Juniper Estates - wanted BRILLIANT website design for our new property investing company

We need a website design for our new company based in Bristol, England, UK called "Juniper Estates". We help buy people property who are in financial difficulty or who are needing to sell their property quickly for reasons such as death, divorce/separation, relocation, emigration.

We have a logo being designed incorporating strawberry and property (so red and green). We would like designs to communicate an elegant ,professional, approachable, friendly
fresh clean but also warm appealing appearance
Not too busy
Website consistent with logo and company name i.e. colour scheme

Please use our word document for content as a guide but use professional judgement for minor alterations if you feel they would benefit the site/structure etc

Please ask at any time if not sure

Target Market(s)

Adult british population, those that have a mortgage / loan / own property

Industry/Entity Type

Financial

Font styles to use
Serif
Sans Serif
Decorative

Colors
0692cd
33b7a4
acd036
fbee3e
3176b5
886aae
a6479a
e567a6
eb1f27

Requirements
Must have
• This must not look like a template website we are looking for UNIQUE please!
Nice to have
• Bristol pictures instead of generic, or colourful line drawings/comic drawings of houses/property/keys/happy people.....
Should not have
• An obvious off the shelf template design

```html
<!DOCTYPE html>
<html lang="en">
<head>
<meta charset="utf-8">
<title>Juniper Estates</title>
<link href="https://fonts.googleapis.com/css2?family=Josefin+Sans:wght@300;400;600&family=Montserrat:wght@500;700&display=swap" rel="stylesheet">
<style>
:root{
  --ink:#111;
  --black:#000;
  --red:#e2231a;
  --green:#8cc43f;
  --green-dark:#5ea22e;
  --olive:#3a3f1c;
  --rule:#8a8a6a;
  --white:#fff;
  --grey:#555;
  --footer:#0d0d0d;
}
*{box-sizing:border-box;margin:0;padding:0}
html,body{width:685px;height:1200px;overflow:hidden}
body{position:relative;font-family:"Josefin Sans",Arial,sans-serif;color:var(--ink);background:var(--white)}
.abs{position:absolute}

.topbar{left:0;top:0;width:685px;height:27px;background:var(--black)}
.contact-strip{left:262px;top:0;width:328px;height:27px;background:#1c1c1c;color:var(--white);font-size:12.5px;white-space:nowrap}
.contact-strip .item{position:absolute;top:0;height:27px;display:flex;align-items:center;gap:8px;white-space:nowrap}

.header{left:0;top:27px;width:685px;height:103px;background:var(--white)}
.brand{left:110px;top:8px;width:140px;display:flex;flex-direction:column;align-items:center;gap:8px}
.brand .dot{width:28px;height:28px;border-radius:50%;background:var(--red)}
.brand .name{font-size:20px;font-weight:400;color:var(--red);white-space:nowrap}
.nav{left:272px;top:49px;display:flex;gap:12px;font-size:10px;white-space:nowrap}
.nav a{color:var(--ink);text-decoration:none;position:relative}
.nav a.active::after{content:"";position:absolute;left:0;right:0;bottom:-7px;height:2px;background:var(--red)}

.hero{left:0;top:130px;width:685px;height:311px;background:linear-gradient(180deg,#8fb3d6 0%,#b9c6c4 30%,#9aa39a 48%,#6f9c3a 62%,#4d8a25 100%)}
.hero-device{left:118px;top:33px;width:168px;height:248px;border-radius:14px;background:linear-gradient(180deg,#f6f6f6,#d8d8d8);border:2px solid #e9e9e9}
.hero-copy{left:330px;top:90px;font-family:"Montserrat",Arial,sans-serif;line-height:1;white-space:nowrap}
.hero-copy .l1{font-size:19px;font-weight:500;color:var(--black)}
.hero-copy .l2{font-size:29px;font-weight:700;color:var(--red);margin-top:6px}
.hero-copy .l3{font-size:18.5px;font-weight:500;color:var(--black);margin-top:3px}
.hero-copy .l4{font-size:27px;font-weight:700;color:var(--green);margin-top:4px}
.btn-hero{left:332px;top:215px;width:145px;height:33px;border-radius:17px;background:var(--olive);border:2px solid var(--white);color:var(--white);font-size:13px;display:flex;align-items:center;justify-content:center}
.dots{left:332px;top:295px;display:flex;gap:4px}
.dots span{width:6px;height:6px;border-radius:50%;background:var(--white)}
.dots span:first-child{background:var(--black)}

.specialise{left:0;top:441px;width:685px;height:216px;background:var(--green)}
.specialise h2{position:absolute;left:0;top:15px;width:685px;text-align:center;color:var(--white);font-weight:400;font-size:17.5px;line-height:24px}
.specialise ul{position:absolute;left:127px;top:80px;list-style:none;font-size:11px;color:#1d2a10;white-space:nowrap}
.specialise li{height:25px}
.specialise li::before{content:"›";color:var(--white);margin-right:9px}
.btn-dark{left:126px;top:180px;width:70px;height:21px;border-radius:11px;background:var(--olive);border:1px solid var(--white);color:var(--white);font-size:11px;display:flex;align-items:center;justify-content:center}
.agent-photo{left:398px;top:66px;width:186px;height:150px;background:linear-gradient(180deg,#8cc43f 0%,#b89a80 30%,#3a3030 60%,#1a1a1a 100%)}

.section-title{left:0;width:685px;text-align:center;font-weight:400;white-space:nowrap}
.listings-title{top:684px;font-size:21px}
.card{top:725px;width:113px}
.card .photo{width:113px;height:75px}
.card .t1{font-size:15px;margin-top:8px;line-height:16px}
.card .t2{font-size:15px;font-weight:300;color:var(--grey);line-height:16px}
.card .rule{height:1px;background:var(--rule);margin-top:7px}

.about-title{top:884px;font-size:24px}
.portrait{top:937px;width:98px;height:98px;border-radius:50%;border:2px solid var(--red)}
.reasons{top:944px;list-style:none;font-size:9px;color:#333;white-space:nowrap}
.reasons li{height:18px}
.reasons li::before{content:"›";color:var(--red);margin-right:8px;font-size:12px}
.btn-small{top:1018px;width:58px;height:17px;border-radius:8px;background:var(--black);border:1px solid var(--red);color:var(--white);font-size:9px;display:flex;align-items:center;justify-content:center}

.footer{left:0;top:1062px;width:685px;height:138px;background:var(--footer);color:var(--white)}
.footer h3{position:absolute;top:10px;font-size:11px;font-weight:400;white-space:nowrap}
.footer .info{position:absolute;font-size:8px;color:#bbb;line-height:10px;white-space:nowrap}
.socials{left:290px;top:29px;display:flex;gap:3px}
.socials span{width:16px;height:16px;border-radius:50%;background:#cfcfcf;border:1px solid #777}
.field{position:absolute;border:1px solid #888;background:#050505;color:#ccc;font-size:7px;padding:2px 3px}
.submit{left:541px;top:94px;width:46px;height:14px;background:#e6e6ee;color:#555;font-size:7px;display:flex;align-items:center;justify-content:center}
.copyright{left:0;top:124px;width:685px;text-align:center;font-size:6px;color:#ccc}
</style>
</head>
<body>

<div class="abs topbar">
  <div class="abs contact-strip">
    <div class="item" style="left:14px">
      <svg width="14" height="14" viewBox="0 0 24 24"><path d="M6.6 10.8a15 15 0 006.6 6.6l2.2-2.2c.3-.3.7-.4 1-.2 1.1.4 2.3.6 3.6.6.6 0 1 .4 1 1V20c0 .6-.4 1-1 1A17 17 0 013 4c0-.6.4-1 1-1h3.5c.6 0 1 .4 1 1 0 1.3.2 2.5.6 3.6.1.3 0 .7-.2 1z" fill="#e2231a"/></svg>
      <span>0117 4960 382</span>
    </div>
    <div class="item" style="left:137px">
      <svg width="16" height="12" viewBox="0 0 16 12"><rect width="16" height="12" fill="#e2231a"/><path d="M0 0l8 6 8-6" fill="none" stroke="#fff" stroke-width="1.2"/></svg>
      <span>hello@juniper-estates.co.uk</span>
    </div>
  </div>
</div>

<div class="abs header">
  <div class="abs brand">
    <span class="dot"></span>
    <span class="name">Juniper Estates</span>
  </div>
  <nav class="abs nav">
    <a class="active" href="#">Home</a>
    <a href="#">Easy Steps</a>
    <a href="#">Rent Property</a>
    <a href="#">Sell Property</a>
    <a href="#">About</a>
    <a href="#">Contact</a>
  </nav>
</div>

<section class="abs hero" role="img" aria-label="Large grey house with a green lawn and trees under a blue sky">
  <div class="abs hero-device" role="img" aria-label="Hand holding a tablet showing the property search app"></div>
  <div class="abs hero-copy">
    <div class="l1">TRACK , MANAGE &amp;</div>
    <div class="l2">GROW YOUR</div>
    <div class="l3">PROPERTY PORTFOLIO</div>
    <div class="l4">THE EASY WAY</div>
  </div>
  <div class="abs btn-hero">View The Property</div>
  <div class="abs dots"><span></span><span></span><span></span></div>
</section>

<section class="abs specialise">
  <h2>We Are A Local Family<br>Run Property Business Who Specialize In</h2>
  <ul>
    <li>Buying properties quickly</li>
    <li>Property rental management</li>
    <li>Chain fixing</li>
    <li>Negative equity problems</li>
  </ul>
  <div class="abs btn-dark">Read More</div>
  <div class="abs agent-photo" role="img" aria-label="Smiling agent in a dark jumper holding up house keys"></div>
</section>

<h2 class="abs section-title listings-title">Properties For Sell And Rent</h2>
<div class="abs card" style="left:97px">
  <div class="photo" role="img" aria-label="Commercial villa with palm trees" style="background:linear-gradient(180deg,#6fa3d6 0%,#9cc0d8 45%,#5f8a3a 70%,#7fa85a 100%)"></div>
  <div class="t1">Commercial</div><div class="t2">Property</div><div class="rule"></div>
</div>
<div class="abs card" style="left:223px">
  <div class="photo" role="img" aria-label="Modern residential house lit up at dusk" style="background:linear-gradient(180deg,#5a5f9a 0%,#3a3550 50%,#c89a5a 72%,#2d2a35 100%)"></div>
  <div class="t1">Residental</div><div class="t2">Property</div><div class="rule"></div>
</div>
<div class="abs card" style="left:349px">
  <div class="photo" role="img" aria-label="Commercial building with columns" style="background:linear-gradient(180deg,#7aa7d8 0%,#d8b27a 40%,#b07a4a 80%,#8a6a4a 100%)"></div>
  <div class="t1">Commercial</div><div class="t2">Property</div><div class="rule"></div>
</div>
<div class="abs card" style="left:475px">
  <div class="photo" role="img" aria-label="Residential bungalow with a pool" style="background:linear-gradient(180deg,#b9d0e6 0%,#c88a6a 40%,#4aa0c0 65%,#7a9a5a 100%)"></div>
  <div class="t1" style="padding-left:15px">Residental</div><div class="t2" style="padding-left:15px">Property</div><div class="rule"></div>
</div>

<h2 class="abs section-title about-title">Who We Are</h2>
<div class="abs portrait" style="left:98px;background:linear-gradient(180deg,#a0553a,#7a4a3a 50%,#2b2b3a)" role="img" aria-label="Couple standing outside a brick house"></div>
<ul class="abs reasons" style="left:205px">
  <li>How to stop repossession</li><li>Divorce or separation</li><li>Financial problems</li><li>Don't like estate agents?</li>
</ul>
<div class="abs btn-small" style="left:207px">Read More</div>
<div class="abs portrait" style="left:362px;background:linear-gradient(180deg,#efe9e0,#c8b49a 50%,#6b5a4a)" role="img" aria-label="Family relaxing at home"></div>
<ul class="abs reasons" style="left:467px">
  <li>How to stop repossession</li><li>Divorce or separation</li><li>Financial problems</li><li>Don't like estate agents?</li>
</ul>
<div class="abs btn-small" style="left:468px">Read More</div>

<footer class="abs footer">
  <h3 style="left:112px">CONTACT</h3>
  <svg class="abs" style="left:108px;top:30px" width="16" height="14" viewBox="0 0 16 14"><path d="M8 0l8 7h-2v7h-4V9H6v5H2V7H0z" fill="#fff"/></svg>
  <div class="info" style="left:128px;top:31px">12 Harbour Lane<br>Bristol BS1 4QA</div>
  <svg class="abs" style="left:110px;top:64px" width="12" height="15" viewBox="0 0 12 15"><rect width="12" height="15" rx="2" fill="#fff"/><rect x="3" y="2" width="6" height="7" fill="#0d0d0d"/></svg>
  <div class="info" style="left:128px;top:63px">0117 4960 382<br>hello@juniper-estates.co.uk</div>

  <h3 style="left:308px">FOLLOW US</h3>
  <div class="abs socials"><span></span><span></span><span></span><span></span><span></span></div>

  <h3 style="left:453px">DROP AS A LINE</h3>
  <div class="field" style="left:453px;top:29px;width:56px;height:14px">Name</div>
  <div class="field" style="left:515px;top:29px;width:72px;height:14px">Email</div>
  <div class="field" style="left:453px;top:50px;width:134px;height:38px">Massage</div>
  <div class="abs submit">Submit</div>
  <div class="abs copyright">Copyright © 2014 All right reserved JUNIPER ESTATES</div>
</footer>

</body>
</html>
```